Veterinary TPLO Surgery Flyer Design

Please use this flyer to make a professional-looking 1 page, double-sided client handout regarding TPLO.

You can visit our website at www.brackenfieldpetcare.com & www.northwoodsanimalsurgerygroup.com for additional logo information. The flyer should include all the text from the one provided.

Target Market(s)

Client communication to for referral surgery between sister veterinary clinics

Industry/Entity Type

Veterinary

Requirements
Must have
• The text included
Nice to have
• Nice to have the Cedar Hollow Avenue Animal CLinic & Dr. Pell Mobile vet logos incorporated.

```html
<!DOCTYPE html>
<html lang="en">
<head>
<meta charset="utf-8">
<title>TPLO Surgery Client Handout</title>
<link href="https://fonts.googleapis.com/css2?family=Montserrat:wght@400;500;600;700;800&display=swap" rel="stylesheet">
<style>
:root{
  --backdrop:#d5d5d5;
  --green:#5e7e6a;
  --navy:#263a78;
  --navy-light:#4a6fa8;
  --white:#ffffff;
  --text-soft:#e9eee9;
  --photo-dark:#2a2a2a;
  --photo-light:#c9c3b5;
}
*{margin:0;padding:0;box-sizing:border-box}
html,body{width:740px;height:1200px;overflow:hidden}
body{background:var(--backdrop);font-family:"Montserrat",sans-serif;color:var(--white);position:relative}
.page{position:absolute;left:178px;width:385px;height:543px;overflow:hidden;box-shadow:4px 6px 10px rgba(0,0,0,.3)}
.page-front{top:42px;background:var(--green)}
.page-back{top:618px;background:var(--navy)}
.page svg.backdrop{position:absolute;left:0;top:0;width:385px;height:543px}
.abs{position:absolute}
h2{font-size:8.4px;font-weight:600;line-height:1.25}
p,li{font-size:5.3px;line-height:1.45;color:var(--text-soft);font-weight:400}
b{font-weight:700;color:var(--white)}
.clinic-mark{left:25px;top:30px;display:flex;align-items:center;gap:6px}
.clinic-mark .dot{width:30px;height:30px;border-radius:50%;background:var(--white);opacity:.9;flex:none}
.clinic-mark .name{font-size:12.5px;font-weight:500;line-height:1.15;color:var(--white)}
.headline{left:25px;top:103px;font-size:7.6px;font-weight:800;line-height:1.35}
.figure{border:1px solid rgba(255,255,255,.6)}
.fig-knee{left:242px;top:151px;width:118px;height:103px;background:linear-gradient(135deg,#cfd3d8,#e8e6df 50%,#b9bec6)}
.fig-xray{left:242px;top:264px;width:118px;height:94px;background:linear-gradient(90deg,var(--photo-dark),#6d6d6d 45%,#9a9a9a 70%,var(--photo-dark))}
.benefits{left:25px;top:387px;width:350px;list-style:none}
.benefits li{position:relative;padding-left:18px;margin-bottom:3.5px}
.benefits li::before{content:"";position:absolute;left:1px;top:2.5px;width:2px;height:2px;border-radius:50%;background:var(--white)}
.surgeon-mark{left:258px;top:38px;width:114px;display:flex;flex-direction:column;align-items:center;gap:5px}
.surgeon-mark .dot{width:42px;height:42px;border-radius:50%;background:var(--navy)}
.surgeon-mark .name{font-size:10px;font-weight:700;color:var(--navy)}
.steps{left:46px;top:158px;width:300px;list-style:none}
.steps li{margin-bottom:5px}
.steps li.gap{margin-bottom:11px}
.followups{left:31px;top:361px;width:330px;list-style:none}
.followups li{position:relative;padding-left:9px;margin-bottom:2.5px}
.followups li::before{content:"";position:absolute;left:1px;top:2.5px;width:2px;height:2px;border-radius:50%;background:var(--text-soft)}
.contact h3{font-size:5.4px;font-weight:700;line-height:1.35;margin-bottom:6px}
.contact p{line-height:1.4}
</style>
</head>
<body>

<section class="page page-front">
  <svg class="backdrop" viewBox="0 0 385 543" aria-hidden="true">
    <defs>
      <linearGradient id="cornerSheen" x1="0" y1="0" x2="1" y2="1">
        <stop offset="0" stop-color="#ffffff"/>
        <stop offset="1" stop-color="#8e8e8e"/>
      </linearGradient>
    </defs>
    <path d="M236,0 C330,10 380,70 385,140 L385,0 Z" fill="url(#cornerSheen)"/>
  </svg>

  <div class="abs clinic-mark">
    <span class="dot"></span>
    <span class="name">Cedar Hollow Avenue<br>Animal Clinic</span>
  </div>

  <h1 class="abs headline">Advanced Orthopedic Care by Dr. Helena Pell, DVM, DACVS-sa<br>TPLO Surgery at Cedar Hollow Avenue Animal Clinic</h1>

  <h2 class="abs" style="left:25px;top:154px">About Dr. Helena Pell</h2>
  <p class="abs" style="left:25px;top:171px;width:196px">Dr. Helena Pell is a board-certified veterinary surgeon (Diplomate of the American College of Veterinary Surgeons) with over 18 years of experience in small animal surgery. A graduate of Great Lakes State University, she completed her surgical residency at Eastbrook School of Veterinary Medicine. Through her mobile practice, Pell Mobile Surgery, Dr. Pell now provides advanced surgical procedures—such as TPLO—directly at local clinics.</p>
  <div class="abs figure fig-knee" role="img" aria-label="Diagram of a canine stifle joint before and after TPLO, showing the tibial plateau angle"></div>

  <h2 class="abs" style="left:25px;top:267px">What is TPLO Surgery?</h2>
  <p class="abs" style="left:25px;top:284px;width:200px">Tibial Plateau Leveling Osteotomy (TPLO) is a surgical procedure that stabilizes the stifle (knee) joint following a cranial cruciate ligament (CCL) rupture—a common orthopedic injury in dogs. The procedure involves altering the angle of the tibial plateau to eliminate abnormal joint motion, restoring stability and improving function.</p>
  <div class="abs figure fig-xray" role="img" aria-label="Pre- and post-operative TPLO radiographs of a dog's knee with bone plate"></div>

  <h2 class="abs" style="left:25px;top:370px">Benefits of TPLO Surgery</h2>
  <ul class="abs benefits">
    <li><b>Enhanced Joint Stability:</b> Restores natural biomechanics, reducing pain and improving mobility.</li>
    <li><b>Faster Recovery:</b> Many dogs return to normal activity faster compared to other surgical techniques.</li>
    <li><b>Proven Long-Term Success:</b> TPLO is particularly effective in large and active breeds.</li>
  </ul>

  <h2 class="abs" style="left:25px;top:454px">Why Choose Cedar Hollow Avenue Animal Clinic?</h2>
  <p class="abs" style="left:25px;top:470px;width:345px">Partnering with Dr. Pell, Cedar Hollow Avenue Animal Clinic offers advanced orthopedic surgery on-site—eliminating the need for referrals or travel. This collaboration ensures your pet receives expert surgical care in a familiar, trusted environment.</p>
  <p class="abs" style="left:25px;top:500px;width:345px">Our clinic works directly with your primary veterinarian to share medical records, diagnostics, and prescriptions, ensuring seamless and coordinated care for your pet.</p>
</section>

<section class="page page-back">
  <svg class="backdrop" viewBox="0 0 385 543" aria-hidden="true">
    <defs>
      <radialGradient id="navyGlow" cx="0.95" cy="0.85" r="0.55">
        <stop offset="0" stop-color="#5a80b8"/>
        <stop offset="1" stop-color="#263a78" stop-opacity="0"/>
      </radialGradient>
    </defs>
    <rect width="385" height="543" fill="url(#navyGlow)"/>
    <path d="M223,0 C235,80 300,138 385,142 L385,0 Z" fill="#ffffff"/>
    <path d="M0,442 C50,428 150,422 185,432 C205,440 225,462 236,478 C230,455 240,436 272,431 C320,425 360,433 385,429 L385,543 L0,543 Z" fill="#5e7e6a"/>
  </svg>

  <div class="abs surgeon-mark">
    <span class="dot"></span>
    <span class="name">Helena Pell</span>
  </div>

  <h2 class="abs" style="left:31px;top:33px">Diagnostic Radiographs vs. TPLO<br>Planning Radiographs</h2>
  <p class="abs" style="left:31px;top:61px;width:198px">While diagnostic radiographs may confirm a CCL tear, they are not sufficient for surgical planning. TPLO requires three advanced technique radiographic views with precise measurements, which must be performed under sedation to reduce discomfort and allow accurate positioning.</p>

  <h2 class="abs" style="left:31px;top:140px">Expected Process</h2>
  <ol class="abs steps">
    <li><b>1. Diagnosis:</b> Your pet is diagnosed with stifle instability (CCL tear) by your veterinarian.</li>
    <li><b>2. Referral:</b> Your veterinarian contacts the surgical coordinator at Cedar Hollow Avenue Animal Clinic.</li>
    <li><b>3. Consultation:</b> The coordinator contacts you to schedule a 1-hour consultation to review the procedure, estimated costs, and available surgery dates.</li>
    <li><b>4. Planning Radiographs:</b> These specialized X-rays are typically taken during the consultation under light sedation.</li>
    <li><b>5. Surgical Review:</b> Dr. Pell reviews the radiographs and your pet's medical history to confirm candidacy for TPLO.</li>
    <li class="gap"><b>6. Deposit:</b> A $3,500 deposit secures Dr. Pell's travel and surgery date. This is refundable if canceled at least 5 days prior to the scheduled procedure.</li>
    <li><b>7. Surgery Day:</b> Your pet is dropped off in the morning and surgery is performed the same day.</li>
    <li><b>8. Discharge:</b> You'll receive a post-surgery update and your pet will go home that evening.</li>
  </ol>

  <h2 class="abs" style="left:31px;top:336px;line-height:1">Post-Operative Care &amp; Follow-Up</h2>
  <p class="abs" style="left:31px;top:345px">Two follow-up appointments will be scheduled:</p>
  <ul class="abs followups">
    <li>4 Weeks Post-Op: Evaluate healing, refill medications, and address any questions.</li>
    <li>8 Weeks Post-Op: Sedated radiographs will confirm proper healing of the surgical site and tibia.</li>
  </ul>
  <p class="abs" style="left:31px;top:387px;width:320px">Dr. Pell will stay in direct contact with you during your pet's recovery using her custom mobile app, which allows for secure messaging and provides detailed post-operative instructions.</p>

  <div class="abs contact" style="left:31px;top:462px">
    <h3>Contact Information:<br>Cedar Hollow Avenue Animal Clinic</h3>
    <p>2240 Cedar Hollow Avenue, Brackenfield, MI 48900<br>(555) 201-4830<br>info@brackenfieldpetcare.com<br>www.brackenfieldpetcare.com</p>
  </div>
  <div class="abs contact" style="left:211px;top:462px">
    <h3>Pell Mobile Surgery<br>(Dr. Helena Pell)</h3>
    <p>(555) 310-6826<br>drpell@northwoodsanimalsurgerygroup.com<br>www.northwoodsanimalsurgerygroup.com</p>
  </div>
</section>

</body>
</html>
```